Business Card Design Z9 MOTORS

Hi firstly I would like you to design a professional logo for my company. By using words " Z9 Auto Spares & Haulage".
We are an auto dismantling company where we buy wrecks/cars for dismantling and selling salvageable parts again.

Hi every one,

Thank you for posting the designs. But unfortunately non of these designs have the logo that I would prefer for my company. I will be branding the logo quite extensively, therefore please design some professional looking ones.

Thanks

Industry/Entity Type

Business

Contact Information for Business Card

Z9 Auto Spares & Haulage, 472 Kowhai Bend Rd, Fernmoor, Wellington
T: 04 7261048, F: 04 7261049, E: dean.morrow@z9motors.example.nz, W: www.z9motors.example.nz
Name: Dean L Morrow
Managing Director
Mob: 027418906

At the bottom of card " WE PAY TOP $$$$ FOR ANY UNWANTED VEHICLES FOR FOR DISMANTLING CALL US NOW 0800372815"

```html
<!DOCTYPE html>
<html lang="en">
<head>
<meta charset="utf-8">
<title>Z9 Auto Spares &amp; Haulage — Business Card</title>
<link rel="stylesheet" href="https://fonts.googleapis.com/css2?family=Libre+Baskerville:ital,wght@0,400;0,700;1,400&family=Oswald:wght@600&display=swap">
<style>
  :root {
    --page-bg: #d9d8d6;
    --panel-dark: #3e3b3c;
    --card-white: #ffffff;
    --brand-red: #e8232f;
    --ink: #2a2a2a;
    --ink-soft: #4a4a4a;
    --on-dark: #f4f4f4;
  }
  * { box-sizing: border-box; margin: 0; padding: 0; }
  html, body {
    width: 1200px; height: 1200px; overflow: hidden;
    background: var(--page-bg);
  }
  .card {
    position: absolute; left: 100px; top: 297px;
    width: 1000px; height: 606px;
    background: var(--card-white);
    box-shadow: 0 10px 30px rgba(0,0,0,.18);
    overflow: hidden;
    font-family: "Libre Baskerville", "Times New Roman", serif;
  }
  .side-panel {
    position: absolute; left: 0; top: 0; bottom: 0; width: 380px;
    background: var(--panel-dark);
    color: var(--on-dark);
    display: flex; flex-direction: column; align-items: center;
    padding-top: 48px;
  }
  .brand-mark {
    width: 150px; height: 150px; border-radius: 50%;
    background: var(--card-white);
  }
  .brand-name {
    margin-top: 22px;
    font-family: "Oswald", "Arial Narrow", sans-serif;
    font-weight: 600; font-size: 27px; letter-spacing: 1px;
    color: var(--on-dark); text-align: center; line-height: 1.2;
  }
  .office-lines { margin-top: 44px; font-size: 24px; line-height: 1.2; }
  .office-lines .label { color: var(--brand-red); font-weight: 700; margin-right: 10px; }
  .address { margin-top: 18px; font-size: 24px; line-height: 1.2; text-align: center; }
  .website {
    margin-top: 18px; font-size: 22px; font-style: italic;
    color: var(--brand-red); letter-spacing: .5px;
  }
  .person {
    position: absolute; right: 70px; top: 70px; text-align: right; color: var(--ink);
  }
  .person-name { font-size: 38px; font-weight: 700; }
  .person-role { font-size: 24px; color: var(--ink-soft); margin-top: 2px; }
  .mobile {
    margin-top: 36px; font-size: 25px;
    display: flex; justify-content: flex-end; align-items: center; gap: 6px;
  }
  .email { margin-top: 14px; font-size: 22px; font-style: italic; color: var(--ink-soft); }
  .offer-band {
    position: absolute; left: 380px; right: 0; bottom: 0; height: 232px;
    background: var(--brand-red); color: var(--card-white);
    font-family: "Oswald", "Arial Narrow", sans-serif; font-weight: 600;
    display: flex; flex-direction: column; justify-content: center; align-items: center;
    text-align: center; padding: 0 30px;
  }
  .offer-text { font-size: 29px; line-height: 1.1; letter-spacing: .5px; }
  .offer-call { margin-top: 14px; font-size: 54px; letter-spacing: 1px; line-height: 1; }
</style>
</head>
<body>
  <article class="card">
    <section class="side-panel">
      <div class="brand-mark"></div>
      <div class="brand-name">Z9 AUTO SPARES<br>&amp; HAULAGE</div>
      <div class="office-lines">
        <div><span class="label">T:</span>04 7261048</div>
        <div><span class="label">F:</span>04 7261049</div>
      </div>
      <div class="address">472 Kowhai Bend Rd<br>Fernmoor, Wellington</div>
      <div class="website">www.z9motors.example.nz</div>
    </section>

    <section class="person">
      <div class="person-name">Dean L. Morrow</div>
      <div class="person-role">Managing Director</div>
      <div class="mobile">
        <svg class="phone-icon" width="30" height="30" viewBox="0 0 30 30" aria-hidden="true">
          <rect x="1" y="1" width="28" height="28" rx="7" fill="#2a2a2a"/>
          <rect x="10" y="6" width="10" height="18" rx="2" fill="none" stroke="#fff" stroke-width="2"/>
          <circle cx="15" cy="21" r="1.2" fill="#fff"/>
        </svg>
        <span>027418906</span>
      </div>
      <div class="email">dean.morrow@z9motors.example.nz</div>
    </section>

    <section class="offer-band">
      <div class="offer-text">WE PAY TOP $$$$ FOR ANY UNWANTED<br>VEHICLES FOR DISMANTLING</div>
      <div class="offer-call">CALL US NOW 0800372815</div>
    </section>
  </article>
</body>
</html>
```